IT Network Consultancy - Business Card

t4 linkways is a IT network consultancy based in London. We're looking for a smart, modern and professional business card design. Our website is here: www.t4linkways.co.uk

Key things that should be included on the card (with examples):

Company Logo
Name
Position / Job Title: Network Consultant
Mobile Phone Number: +44 (0) 7700 900418
Land Line: +44 (0) 1632 960274
Email Address: name@t4linkways.co.uk
Web Site URL: www.t4linkways.co.uk

Target Market(s)

Large enterprise / global companies / corporates

Industry/Entity Type

Business

Requirements
Must have
• Incorporate our logo - which is attached to the project. They are in AI format (can be opened in Inkscape).

The design should be double sided and fit on a UK standard 85mm × 55mm card and be in a format that retains the quality when printed.
Nice to have
• The project does not have to conform to the colour of our website but this should give you inspiration of the style we like.
Should not have
• Bright colours. Pictures are not necessary.

```html
<!DOCTYPE html>
<html lang="en">
<head>
<meta charset="utf-8">
<title>t4 linkways – Business Card</title>
<link rel="stylesheet" href="https://fonts.googleapis.com/css2?family=Montserrat:wght@300;400;500;700&display=swap">
<style>
  :root {
    --backdrop: #a9b1b1;
    --card: #ffffff;
    --navy: #1b2240;
    --slate: #6d7275;
    --ink-soft: #5c6366;
    --ice: rgba(200, 228, 238, 0.9);
    --ice-deep: rgba(150, 196, 214, 0.85);
    --people: rgba(58, 69, 96, 0.45);
  }
  * { box-sizing: border-box; margin: 0; padding: 0; }
  html, body {
    width: 1043px; height: 1200px; overflow: hidden;
    background: var(--backdrop);
    font-family: "Montserrat", sans-serif;
  }
  .sheet { position: relative; width: 1043px; height: 1200px; }
  .card {
    position: absolute; left: 19px; width: 1005px; height: 570px;
    background: var(--card); border-radius: 34px; overflow: hidden;
  }
  .card--front { top: 19px; }
  .card--back { top: 611px; }

  .artwork {
    position: absolute;
    background:
      radial-gradient(ellipse closest-side at 50% 50%, var(--people) 0%, rgba(58,69,96,0) 55%),
      radial-gradient(ellipse closest-side at 50% 50%, var(--ice-deep) 0%, var(--ice) 45%, rgba(214,235,241,0) 100%);
  }
  .card--front .artwork { left: -60px; top: -40px; width: 480px; height: 560px; }
  .card--back .artwork { left: 700px; top: 20px; width: 360px; height: 560px; }

  .brand {
    position: absolute; color: var(--navy);
    font-weight: 400; letter-spacing: 2px; white-space: nowrap; line-height: 1;
  }
  .card--front .brand { left: 313px; top: 108px; font-size: 90px; }
  .card--back .brand { left: 85px; top: 196px; font-size: 90px; }

  .person { position: absolute; left: 375px; top: 330px; }
  .person__name {
    font-weight: 700; font-size: 35.5px; color: var(--navy);
    letter-spacing: 1.5px; line-height: 1; white-space: nowrap;
  }
  .person__role {
    margin-left: 133px; margin-top: 5px;
    font-weight: 500; font-size: 18px; color: var(--slate); letter-spacing: 1.2px;
    white-space: nowrap;
  }

  .contact {
    position: absolute; left: 440px; top: 402px;
    display: grid; grid-template-columns: 148px 30px auto; row-gap: 5px;
    align-items: center;
  }
  .contact__label {
    text-align: right; font-weight: 700; font-size: 14px;
    color: var(--navy); letter-spacing: 0.6px;
  }
  .contact__dot { text-align: center; color: var(--navy); font-size: 18px; line-height: 1; }
  .contact__value {
    font-weight: 500; font-size: 20.5px; color: var(--ink-soft); letter-spacing: 1px;
    white-space: nowrap;
  }

  .web-address {
    position: absolute; left: 129px; top: 305px;
    font-weight: 700; font-size: 22px; color: var(--slate); letter-spacing: 12px;
    white-space: nowrap;
  }
</style>
</head>
<body>
<main class="sheet">

  <section class="card card--front" aria-label="Card front">
    <div class="artwork" role="img" aria-label="Illustration of business people standing on pale blue jigsaw puzzle pieces"></div>
    <div class="brand">t4 linkways</div>
    <div class="person">
      <p class="person__name">FIRST, LASTNAME</p>
      <p class="person__role">NETWORK CONSULTANT</p>
    </div>
    <div class="contact">
      <span class="contact__label">MOBILE</span><span class="contact__dot">•</span><span class="contact__value">+44 (0) 7700 900418</span>
      <span class="contact__label">LANDLINE</span><span class="contact__dot">•</span><span class="contact__value">+44 (0) 1632 960274</span>
      <span class="contact__label">EMAIL</span><span class="contact__dot">•</span><span class="contact__value">NAME@T4LINKWAYS.CO.UK</span>
      <span class="contact__label">WEBSITE</span><span class="contact__dot">•</span><span class="contact__value">T4LINKWAYS.CO.UK</span>
    </div>
  </section>

  <section class="card card--back" aria-label="Card back">
    <div class="artwork" role="img" aria-label="Illustration of business people standing on pale blue jigsaw puzzle pieces"></div>
    <div class="brand">t4 linkways</div>
    <p class="web-address">WWW.T4LINKWAYS.CO.UK</p>
  </section>

</main>
</body>
</html>
```